1/2 page ad, 1/2 HORIZONTAL 9.875" x 5", for magazine

We need an ad design that tastefully describes the services we offer.

The Lindenmoor Heritage Hall is the heart of Vancouver. We provide classic, updated banquet halls with integrated audio visual capabilities and soaring ceilings. With nine rental halls we are home for international conferences, intimate family gatherings and celebrations for up to 1400 people. Our central location, free parking and full service catering are an ideal solution for weddings, celebrations of life and Christmas parties. With break out rooms and separate rooms for dining and meeting, we are a tremendous asset for the Vancouver destination conferences, awards nights and ceremonies.

1. A PDF x/1a file (CMYK, all fonts embedded, images 200ppi) Black or grey recommended
% of black only.
2. An Illustrator CS6 (or lower) file or eps file with all fonts converted to outlines and all
images embedded. Colour space must be CMYK, not RGB. Images should be 200ppi

```html
<!DOCTYPE html>
<html lang="en">
<head>
<meta charset="utf-8">
<title>Lindenmoor Heritage Hall – The Heart of Vancouver</title>
<link href="https://fonts.googleapis.com/css2?family=Poppins:wght@400;500;600;700;800;900&display=swap" rel="stylesheet">
<style>
  :root{
    --navy:#2e3189;
    --red:#e63a30;
    --red-dark:#b8231c;
    --ink:#1b1b1b;
    --white:#ffffff;
    --stage:#d6d6d6;
    --photo-warm:#d9b48f;
    --photo-light:#efe6da;
  }
  *{margin:0;padding:0;box-sizing:border-box}
  html,body{width:673px;height:1200px;overflow:hidden}
  body{background:var(--stage);font-family:"Poppins",sans-serif;position:relative;color:var(--ink)}
  .ad{position:absolute;background:var(--white);overflow:hidden;box-shadow:0 4px 10px rgba(0,0,0,.25)}
  .abs{position:absolute}
  .tick{position:absolute;width:8px;height:8px}
  .brand-seal{position:absolute;border-radius:50%;border:1.5px solid var(--navy);display:flex;align-items:center;justify-content:center;text-align:center;color:var(--navy);font-weight:700;line-height:1.15}

  /* Horizontal ad */
  .ad-wide{left:68px;top:78px;width:531px;height:268px}
  .ad-wide .brand-seal{left:15px;top:22px;width:65px;height:65px;font-size:8px}
  .ad-wide .title{position:absolute;left:92px;top:20px;font-weight:800;font-size:36px;line-height:31px;letter-spacing:-1px}
  .ad-wide .title .l1{color:var(--ink);display:block}
  .ad-wide .title .l2{color:var(--red);display:block}
  .ad-wide .band{position:absolute;left:0;top:103px;width:531px;height:123px;background:var(--navy)}
  .ad-wide .photo{position:absolute;left:0;top:0;width:531px;height:268px}
  .ad-wide .ribbon{position:absolute;left:86px;top:93px;width:176px;height:24px}
  .ad-wide .ribbon-text{position:absolute;left:86px;top:93px;width:176px;height:22px;line-height:22px;text-align:center;color:var(--white);font-weight:700;font-size:12px}
  .ad-wide .item{position:absolute;color:var(--white);font-size:6px;line-height:7.4px}
  .ad-wide .item b{font-weight:700;font-size:7px;line-height:8.8px;display:block}
  .ad-wide .item .lead{font-size:6px}
  .ad-wide .foot{position:absolute;top:233px;height:22px;line-height:22px;font-size:15px}
  .ad-wide .call{left:21px;font-weight:700}
  .ad-wide .phone{left:151px;font-weight:600;letter-spacing:.3px}
  .ad-wide .url{left:289px;font-size:15px;font-weight:400}
  .ad-wide .url b{font-weight:600}

  /* Vertical ad */
  .ad-tall{left:74px;top:382px;width:525px;height:746px}
  .ad-tall .photo{position:absolute;left:0;top:0;width:525px;height:254px}
  .ad-tall .band{position:absolute;left:0;top:254px;width:525px;height:144px;background:var(--navy)}
  .ad-tall .title{position:absolute;left:56px;top:272px;color:var(--white);font-weight:800;font-size:58px;line-height:54px;letter-spacing:-1.5px}
  .ad-tall .frame{position:absolute;left:23px;top:427px;width:479px;height:215px;border:1.5px solid var(--red);border-radius:9px}
  .ad-tall .ribbon{position:absolute;left:115px;top:404px;width:296px;height:40px}
  .ad-tall .ribbon-text{position:absolute;left:115px;top:406px;width:296px;height:36px;line-height:38px;text-align:center;color:var(--white);font-weight:700;font-size:21px}
  .ad-tall .tick{width:10px;height:10px}
  .ad-tall .item{position:absolute;font-size:10.5px;line-height:12px;color:var(--ink)}
  .ad-tall .item b{font-weight:700;font-size:12.5px;line-height:15px;color:var(--navy);display:block}
  .ad-tall .brand-seal{left:29px;top:657px;width:73px;height:73px;font-size:9px}
  .ad-tall .phone{position:absolute;left:154px;top:648px;font-weight:700;font-size:47px;line-height:50px;color:var(--red);letter-spacing:1px}
  .ad-tall .url{position:absolute;left:160px;top:696px;font-weight:600;font-size:24px;line-height:28px;color:var(--ink)}
</style>
</head>
<body>

<svg width="0" height="0" style="position:absolute">
  <defs>
    <symbol id="tick" viewBox="0 0 10 10">
      <circle cx="5" cy="5" r="4.3" fill="none" stroke="currentColor" stroke-width="0.8"/>
      <path d="M3 5.1 L4.5 6.5 L7.1 3.7" fill="none" stroke="currentColor" stroke-width="0.9"/>
    </symbol>
    <symbol id="phone" viewBox="0 0 24 24">
      <path d="M6.6 2.5 L9.4 6.8 L7.6 9 C8.7 11.6 12.4 15.3 15 16.4 L17.2 14.6 L21.5 17.4 L19.6 21 C11.8 21 3 12.2 3 4.4 Z" fill="currentColor"/>
      <path d="M14 3.5 A7 7 0 0 1 20.5 10 M14 7 A3.5 3.5 0 0 1 17 10" fill="none" stroke="currentColor" stroke-width="1.6"/>
    </symbol>
    <symbol id="globe" viewBox="0 0 24 24">
      <circle cx="12" cy="12" r="10" fill="currentColor"/>
      <path d="M2 12 H22 M12 2 C7 7 7 17 12 22 M12 2 C17 7 17 17 12 22 M4 7 H20 M4 17 H20" fill="none" stroke="#fff" stroke-width="1.1"/>
    </symbol>
  </defs>
</svg>

<!-- Horizontal half-page ad -->
<section class="ad ad-wide">
  <div class="brand-seal">Lindenmoor<br>Heritage<br>Hall</div>
  <h1 class="title"><span class="l1">THE HEART OF</span><span class="l2">VANCOUVER</span></h1>

  <div class="band"></div>
  <svg class="photo" viewBox="0 0 531 268">
    <defs>
      <linearGradient id="hallWide" x1="0" y1="0" x2="0" y2="1">
        <stop offset="0" stop-color="#f3eee6"/>
        <stop offset="0.5" stop-color="#e6d6c2"/>
        <stop offset="1" stop-color="#c98c62"/>
      </linearGradient>
    </defs>
    <circle cx="530" cy="62" r="172" fill="#ffffff"/>
    <circle cx="530" cy="62" r="168" fill="url(#hallWide)" role="img" aria-label="Photo of a banquet hall set for a wedding with round tables and gold chairs"/>
  </svg>

  <svg class="ribbon" viewBox="0 0 176 24" preserveAspectRatio="none">
    <path d="M0 0 H30 V20 H8 Z" fill="var(--red-dark)"/>
    <path d="M176 0 H146 V20 H168 Z" fill="var(--red-dark)"/>
    <rect x="16" y="1" width="144" height="22" rx="11" fill="var(--red)"/>
  </svg>
  <div class="ribbon-text">SERVICES WE OFFER</div>

  <svg class="tick" style="left:18px;top:134px;color:#fff"><use href="#tick"/></svg>
  <div class="item" style="left:29px;top:132px;width:150px"><b>WE PROVIDE CLASSIC, UPDATED BANQUET HALLS</b>with integrated audio visual capabilities and soaring ceilings.</div>

  <svg class="tick" style="left:171px;top:134px;color:#fff"><use href="#tick"/></svg>
  <div class="item" style="left:183px;top:132px;width:160px"><b>OUR CENTRAL LOCATION, FREE PARKING AND FULL SERVICE CATERING</b>are an ideal solution for weddings, celebrations of life and Christmas parties.</div>

  <svg class="tick" style="left:18px;top:173px;color:#fff"><use href="#tick"/></svg>
  <div class="item" style="left:29px;top:171px;width:150px"><b>NINE RENTAL HALLS WE ARE HOME</b>for international conferences.</div>

  <svg class="tick" style="left:171px;top:173px;color:#fff"><use href="#tick"/></svg>
  <div class="item" style="left:183px;top:171px;width:170px"><b>BREAK OUT ROOMS AND SEPARATE ROOMS</b>for dining and meeting.</div>

  <svg class="tick" style="left:18px;top:195px;color:#fff"><use href="#tick"/></svg>
  <div class="item" style="left:28px;top:192px;width:150px"><span class="lead">we are a tremendous asset for the Vancouver</span><b>DESTINATION CONFERENCES, AWARDS NIGHTS AND CEREMONIES.</b></div>

  <svg class="tick" style="left:171px;top:195px;color:#fff"><use href="#tick"/></svg>
  <div class="item" style="left:183px;top:193px;width:160px"><span class="lead">Intimate family gatherings and celebrations for</span><b>UP TO 1400 PEOPLE</b></div>

  <div class="foot call">Call Us Now!</div>
  <svg class="abs" style="left:132px;top:237px;width:14px;height:14px;color:var(--red)"><use href="#phone"/></svg>
  <div class="foot phone">604-555-0187</div>
  <svg class="abs" style="left:270px;top:237px;width:13px;height:13px;color:var(--red)"><use href="#globe"/></svg>
  <div class="foot url">www.<b>lindenmoorhall</b>.com</div>
</section>

<!-- Vertical ad -->
<section class="ad ad-tall">
  <div class="photo" role="img" aria-label="Photo of a banquet hall set for a wedding with round tables, white linens and gold chairs" style="background:linear-gradient(180deg,#f2efea 0%,#e8ddd0 40%,#ead6bf 60%,#c98c62 100%)"></div>

  <div class="band"></div>
  <h1 class="title">THE HEART OF<br>VANCOUVER</h1>

  <div class="frame"></div>
  <svg class="ribbon" viewBox="0 0 296 40" preserveAspectRatio="none">
    <path d="M0 0 H50 V34 H12 Z" fill="var(--red-dark)"/>
    <path d="M296 0 H246 V34 H284 Z" fill="var(--red-dark)"/>
    <rect x="28" y="2" width="240" height="36" rx="18" fill="var(--red)"/>
  </svg>
  <div class="ribbon-text">SERVICES WE OFFER</div>

  <svg class="tick" style="left:38px;top:466px;color:var(--navy)"><use href="#tick"/></svg>
  <div class="item" style="left:53px;top:463px;width:220px"><b>WE PROVIDE CLASSIC, UPDATED BANQUET HALLS</b>with integrated audio visual capabilities and soaring ceilings.</div>

  <svg class="tick" style="left:38px;top:532px;color:var(--navy)"><use href="#tick"/></svg>
  <div class="item" style="left:53px;top:529px;width:220px"><b>NINE RENTAL HALLS WE<br>ARE HOME</b>for international conferences.</div>

  <svg class="tick" style="left:38px;top:568px;color:var(--navy)"><use href="#tick"/></svg>
  <div class="item" style="left:53px;top:584px;width:220px">we are a tremendous asset for the<b>VANCOUVER DESTINATION CONFERENCES, AWARDS NIGHTS AND CEREMONIES.</b></div>

  <svg class="tick" style="left:268px;top:466px;color:var(--navy)"><use href="#tick"/></svg>
  <div class="item" style="left:283px;top:463px;width:215px"><b>OUR CENTRAL LOCATION, FREE PARKING AND FULL SERVICE CATERING</b>are an ideal solution for weddings, celebrations of life and Christmas parties.</div>

  <svg class="tick" style="left:268px;top:547px;color:var(--navy)"><use href="#tick"/></svg>
  <div class="item" style="left:283px;top:544px;width:215px"><b>BREAK OUT ROOMS AND<br>SEPARATE ROOMS</b>for dining and meeting.</div>

  <svg class="tick" style="left:268px;top:600px;color:var(--navy)"><use href="#tick"/></svg>
  <div class="item" style="left:283px;top:597px;width:215px">Intimate family gatherings and celebrations for<b>UP TO 1400 PEOPLE</b></div>

  <div class="brand-seal">Lindenmoor<br>Heritage<br>Hall</div>
  <svg class="abs" style="left:120px;top:660px;width:26px;height:26px;color:var(--red)"><use href="#phone"/></svg>
  <div class="phone">604-555-0187</div>
  <svg class="abs" style="left:124px;top:700px;width:23px;height:23px;color:var(--red)"><use href="#globe"/></svg>
  <div class="url">www.lindenmoorhall.com</div>
</section>

</body>
</html>
```